Business Card Design Project

We recently redesigned our corporate logo and are looking for a business card refreshment.

The business card template should have a place for the following:
Name, Title, email, phone number, instant messenger handle, and the vitals of the company such as the address, main line, web site etc.

PLEASE DO NOT USE OUR EXISTING WEB SITE FOR INSPIRATION as we are redesigning it.

We've attached a picture of our existing business card as an example, although please keep in mind that we have changed the logo (also attached) and encourage your creativity.

Target Market(s)

Information scientists, search professionals, technical people, Ph.Ds, and executives

Industry/Entity Type

Business

Requirements
Must have
• We'll need the template in a format like Illustrator.

```html
<!DOCTYPE html>
<html lang="en">
<head>
<meta charset="utf-8">
<title>HelixScope Business Card</title>
<link rel="stylesheet" href="https://fonts.googleapis.com/css2?family=Source+Sans+3:wght@400;700&display=swap">
<style>
  :root {
    --backdrop: #e6e7e7;
    --paper: #f4f5f5;
    --slate: #5f6968;
    --slate-light: #87928f;
    --brand-blue: #1680bd;
    --brand-blue-bright: #22a6dc;
    --text-light: #f2f4f4;
    --divider: #a7b0ae;
  }
  * { box-sizing: border-box; margin: 0; padding: 0; }
  html, body {
    width: 1200px; height: 900px; overflow: hidden;
    background: radial-gradient(circle at 50% 45%, #f6f6f6 0%, var(--backdrop) 75%);
    font-family: "Source Sans 3", "Myriad Pro", sans-serif;
  }
  .canvas { position: relative; width: 1200px; height: 900px; }
  .card {
    position: absolute; width: 525px; height: 300px; overflow: hidden;
    box-shadow: 0 10px 28px rgba(0,0,0,.22);
  }
  .logo {
    display: flex; align-items: center; gap: 8px;
    font-weight: 700; letter-spacing: -0.5px;
  }
  .logo-dot { border-radius: 50%; flex: none; }

  /* Back side */
  .card-back {
    left: 338px; top: 80px;
    background: linear-gradient(135deg, var(--slate) 0%, var(--slate-light) 55%, var(--slate) 100%);
    display: flex; align-items: center; justify-content: center;
  }
  .card-back .logo { color: var(--brand-blue-bright); font-size: 34px; }
  .card-back .logo-dot { width: 26px; height: 26px; background: var(--brand-blue-bright); }

  /* Front side */
  .card-front { left: 338px; top: 500px; background: var(--slate); }
  .front-top {
    position: absolute; left: 0; top: 0; width: 100%; height: 120px;
    background: var(--paper);
  }
  .front-top .logo {
    position: absolute; left: 38px; top: 48px;
    color: var(--brand-blue); font-size: 36px;
  }
  .front-top .logo-dot { width: 28px; height: 28px; background: var(--brand-blue); }
  .accent-rule {
    position: absolute; left: 0; top: 120px; width: 100%; height: 5px;
    background: var(--brand-blue);
  }
  .front-body {
    position: absolute; left: 0; top: 125px; width: 100%; height: 175px;
    background: linear-gradient(120deg, #566160 0%, #6f7a78 60%, #5a6463 100%);
  }
  .name-tab { position: absolute; left: 446px; top: 124px; }
  .holder { position: absolute; right: 36px; top: 140px; text-align: right; }
  .holder-name { color: var(--brand-blue-bright); font-weight: 700; font-size: 15px; }
  .holder-title { color: var(--text-light); font-size: 12px; }
  .column-divider {
    position: absolute; left: 330px; top: 155px; width: 1px; height: 120px;
    background: var(--divider);
  }
  .contact-list {
    position: absolute; left: 40px; top: 160px; list-style: none;
    color: var(--text-light); font-size: 12px; line-height: 15px;
  }
  .contact-list li { display: flex; align-items: flex-start; gap: 10px; margin-bottom: 3px; }
  .contact-list svg { flex: none; width: 14px; height: 14px; margin-top: 1px; }
</style>
</head>
<body>
<main class="canvas">

  <section class="card card-back" aria-label="Card back">
    <div class="logo"><span class="logo-dot"></span>HelixScope</div>
  </section>

  <section class="card card-front" aria-label="Card front">
    <div class="front-top">
      <div class="logo"><span class="logo-dot"></span>HelixScope</div>
    </div>
    <div class="accent-rule"></div>
    <div class="front-body"></div>

    <svg class="name-tab" width="26" height="12" viewBox="0 0 26 12" aria-hidden="true">
      <polygon points="0,0 26,0 13,12" fill="#1680bd"/>
    </svg>
    <div class="holder">
      <p class="holder-name">Daniel Morrow</p>
      <p class="holder-title">Director</p>
    </div>

    <div class="column-divider"></div>

    <ul class="contact-list">
      <li>
        <svg viewBox="0 0 14 14" aria-hidden="true"><circle cx="7" cy="7" r="7" fill="#1680bd"/><path d="M7 3.2a2.4 2.4 0 0 1 2.4 2.4C9.4 7.4 7 10.6 7 10.6S4.6 7.4 4.6 5.6A2.4 2.4 0 0 1 7 3.2z" fill="#fff"/><circle cx="7" cy="5.6" r=".9" fill="#1680bd"/></svg>
        <span>Kastanjelaan 22-B4<br>5678 CD, Zwolle</span>
      </li>
      <li>
        <svg viewBox="0 0 14 14" aria-hidden="true"><circle cx="7" cy="7" r="7" fill="#1680bd"/><path d="M4.3 3.6l1.6-.3.8 1.9-1 .7a5 5 0 0 0 2.4 2.4l.7-1 1.9.8-.3 1.6C8 10 3.9 6 4.3 3.6z" fill="#fff"/></svg>
        <span>555-014-2210</span>
      </li>
      <li>
        <svg viewBox="0 0 14 14" aria-hidden="true"><circle cx="7" cy="7" r="7" fill="#1680bd"/><rect x="4.5" y="3.5" width="5" height="2.5" fill="#fff"/><rect x="3.5" y="6" width="7" height="3" rx=".5" fill="#fff"/><rect x="4.5" y="8.5" width="5" height="2" fill="#fff"/></svg>
        <span>555-014-2219</span>
      </li>
      <li>
        <svg viewBox="0 0 14 14" aria-hidden="true"><circle cx="7" cy="7" r="7" fill="#1680bd"/><text x="7" y="10" text-anchor="middle" font-size="9" font-weight="700" fill="#fff" font-family="sans-serif">@</text></svg>
        <span>daniel@helixscope.com</span>
      </li>
      <li>
        <svg viewBox="0 0 14 14" aria-hidden="true"><circle cx="7" cy="7" r="7" fill="#1680bd"/><circle cx="7" cy="7" r="3.6" fill="none" stroke="#fff" stroke-width="1"/><ellipse cx="7" cy="7" rx="1.5" ry="3.6" fill="none" stroke="#fff" stroke-width=".8"/><line x1="3.4" y1="7" x2="10.6" y2="7" stroke="#fff" stroke-width=".8"/></svg>
        <span>www.helixscope.com</span>
      </li>
    </ul>
  </section>

</main>
</body>
</html>
```